Corwith Lodge website redesign

After 8 years of our current site, we're ready to upgrade our site design. We'd like to generally make it more modern and clean and build it on a CMS like joomla for easier future maintenance.

Our hotel is a family-owned bed and breakfast that competes against much larger hotel chains in Aspen with fancier rooms and larger pricetags. Our hotel is priced moderately and features tasteful, uniquely-design rooms.

We are looking for a website that will showcase the uniqueness of our rooms, the history of the Lodge, and the friendliness of our staff.

Here are some other hotel sites we like:

http://www.brackenfoldhouse.example/

http://www.tollerpeakhaus.example/

http://www.quarrowstay.example/

*********

Scope of Work - I'm looking for a design AND build. The website should be built out in Joomla as part of the final deliverable.
Updates

Current website: http://www.corwithlodge.example/

Explanation of what design + build means:

I am looking for not only the design of the site, but also for the homepage and one subpage to be built out as well. I do NOT need the entire site built - only for those two pages to be built and I will retrofit the remainder of the pages.

Target Market(s)

travellers evaluating hotels in Aspen, Colorado.

Industry/Entity Type

Hotel

Requirements
Must have
• Must, must, must be based on a joomla template. "Rotating" large main image as central position on homepage is a must (see example websites mentioned above).

Nice to have
• We have an existing online reservation system. It would be nice to evaluate placing a "widget" on the homepage that integrates to the online reservation page. Similar to that feature that the Bracken Fold website has at the foot of the main image on their homepage.

```html
<!DOCTYPE html>
<html lang="en">
<head>
<meta charset="utf-8">
<title>Corwith Lodge</title>
<link href="https://fonts.googleapis.com/css2?family=Source+Sans+3:wght@400;600&display=swap" rel="stylesheet">
<style>
:root{
  --brick:#8c3a28;
  --brick-dark:#6b2819;
  --brick-mid:#7c3222;
  --brick-light:#a24a33;
  --title:#9a3c28;
  --ink:#2b1a14;
  --paper:#ffffff;
  --line:#c98a76;
  --cream:#f3e6e0;
}
*{box-sizing:border-box;margin:0;padding:0}
html,body{width:1200px;height:1118px;overflow:hidden}
body{position:relative;background:var(--paper);font-family:"Source Sans 3",sans-serif;color:var(--ink)}
.abs{position:absolute}
.header{left:0;top:0;width:1200px;height:109px;background:var(--brick)}
.logo{left:240px;top:56px;font-size:26px;font-weight:400;color:var(--paper);letter-spacing:.5px}
.utility{top:36px;font-size:10.5px;color:var(--paper);display:flex;align-items:center;gap:5px}
.search{left:736px;top:65px;width:213px;height:31px;background:var(--brick-mid);border-radius:3px;color:var(--paper);font-size:10.5px;padding:9px 14px}
.search svg{position:absolute;right:14px;top:9px}
.nav{left:0;top:109px;width:1200px;height:44px;background:var(--brick-dark);border-bottom:5px solid var(--brick-light)}
.nav ul{list-style:none;display:flex;position:absolute;left:234px;top:13px;gap:0}
.nav li{color:var(--paper);font-size:12px;margin-right:25.8px}
.hero{left:0;top:158px;width:1200px;height:418px;background:linear-gradient(180deg,#4a3a32 0%,#7a4a2e 40%,#a0724e 70%,#3e2c24 100%)}
.hero-arrow{top:336px}
.reserve{left:227px;top:551px;width:731px;height:55px;background:var(--paper);border-radius:5px;box-shadow:0 1px 3px rgba(0,0,0,.35)}
.reserve-tab{left:0;top:0}
.reserve-title{left:17px;top:8px;color:var(--paper);font-size:17px;line-height:14px}
.field-label{top:21px;font-size:11.5px;color:var(--title)}
.field{top:17px;height:20px;border:1px solid var(--line);border-radius:4px;background:var(--paper)}
.select{font-size:10px;color:var(--title);padding:3px 6px}
.select svg{position:absolute;right:6px;top:7px}
.btn{background:var(--brick);color:var(--paper);font-size:11px;border-radius:3px;text-align:center}
.welcome-title{left:228px;top:628px;font-size:20px;color:var(--title);font-weight:400}
.welcome-text{left:228px;top:662px;width:256px;font-size:8.6px;line-height:11px;text-align:justify}
.welcome-text p{margin-bottom:10px}
.badge{border:1px solid #7aa86a}
.tour{left:500px;top:757px;font-size:8.6px;line-height:11px;color:var(--title);text-decoration:underline}
.offer{left:751px;top:632px;width:206px;height:150px;background:var(--cream);border-radius:5px;padding:4px}
.offer-photo{width:198px;height:142px;background:linear-gradient(180deg,#6b4630 0%,#8a5a3c 45%,#a8523f 70%,#5b3a2a 100%);position:relative}
.offer-band{position:absolute;left:0;bottom:0;width:198px;height:46px;background:rgba(60,35,25,.55)}
.offer-heading{position:absolute;left:14px;top:10px;font-size:25px;color:var(--paper);font-weight:600}
.offer-small{position:absolute;left:14px;bottom:9px;font-size:12.5px;line-height:15px;color:var(--paper)}
.offer-free{position:absolute;right:10px;bottom:7px;font-size:30px;font-weight:600;color:var(--paper);letter-spacing:-.5px}
.band{left:0;top:800px;width:1200px;height:242px;background:var(--brick)}
.col-title{top:820px;font-size:18px;color:var(--paper);font-weight:600}
.band-text{font-size:10px;color:var(--paper);line-height:13px}
.band-list{list-style:none;left:230px;top:895px;width:195px}
.band-list li{position:relative;padding-left:11px}
.band-list li::before{content:">";position:absolute;left:0}
.band-btn{top:998px;width:83px;height:27px;background:var(--brick-dark);color:var(--paper);font-size:11px;text-align:center;line-height:27px;border-radius:2px}
.gallery{left:493px;top:859px;width:203px;height:117px;background:var(--paper);border-radius:3px}
.event-date{left:751px;width:36px;height:30px;background:var(--brick-dark);color:var(--paper);text-align:center;font-size:11px;line-height:11px;padding-top:4px}
.event-date small{display:block;font-size:7px;line-height:10px}
.event-text{left:800px;width:170px;font-size:9px;line-height:13.5px;color:var(--paper)}
.footer-links{left:227px;top:1061px;font-size:9px;line-height:14px;color:var(--title)}
.social-label{left:775px;top:1071px;font-size:9px;color:var(--ink)}
.social{top:1063px;width:26px;height:26px;border-radius:50%;background:var(--brick)}
</style>
</head>
<body>
<header class="abs header">
  <div class="abs logo">Corwith Lodge</div>
  <div class="abs utility" style="left:821px">
    <svg width="13" height="9" viewBox="0 0 13 9"><rect width="13" height="9" fill="#e9c9bd"/><path d="M0 0l6.5 5L13 0" stroke="#8c3a28" fill="none"/></svg>Email</div>
  <div class="abs utility" style="left:881px">
    <svg width="11" height="9" viewBox="0 0 11 9"><path d="M0 3Q5.5-1 11 3L9 4 7 3V2H4v1L2 4Z M2 5h7v4H2Z" fill="#fff"/></svg>Contact Us</div>
  <div class="abs search">Search
    <svg width="12" height="12" viewBox="0 0 12 12"><circle cx="5" cy="5" r="3.5" stroke="#fff" stroke-width="1.8" fill="none"/><path d="M7.5 7.5L11 11" stroke="#fff" stroke-width="2"/></svg>
  </div>
</header>
<nav class="abs nav">
  <ul>
    <li>About the inn</li><li>Rooms</li><li>Reservations</li><li>Amenities</li><li>Aspen Information</li><li>Manager’s</li><li>Journal</li><li>Webcams</li><li>Contact Us</li>
  </ul>
</nav>
<div class="abs hero" role="img" aria-label="Rotating photo: snow-covered lodge entrance with timber porch, stone pillars and glowing lanterns at dusk"></div>
<svg class="abs hero-arrow" style="left:228px" width="26" height="46" viewBox="0 0 26 46"><path d="M24 0L4 23l20 23h-6L0 23 18 0Z" fill="#8c3a28" opacity=".85"/></svg>
<svg class="abs hero-arrow" style="left:930px" width="26" height="46" viewBox="0 0 26 46"><path d="M2 0l20 23L2 46h6l18-23L8 0Z" fill="#8c3a28" opacity=".85"/></svg>

<section class="abs reserve">
  <svg class="abs reserve-tab" width="128" height="55" viewBox="0 0 128 55"><path d="M5 0H110L128 27.5 110 55H5Q0 55 0 50V5Q0 0 5 0Z" fill="#8c3a28"/></svg>
  <div class="abs reserve-title">Quick<br><span style="margin-left:-9px">Reservation</span></div>
  <div class="abs field-label" style="left:137px">Arrival:</div>
  <div class="abs field" style="left:174px;width:102px"></div>
  <div class="abs field-label" style="left:288px">Departure:</div>
  <div class="abs field" style="left:342px;width:102px"></div>
  <div class="abs field-label" style="left:456px">Adults:</div>
  <div class="abs field select" style="left:494px;width:40px">00<svg width="6" height="4" viewBox="0 0 6 4"><path d="M0 0l3 3 3-3" stroke="#9a3c28" fill="none"/></svg></div>
  <div class="abs field-label" style="left:547px">Children:</div>
  <div class="abs field select" style="left:594px;width:42px">00<svg width="6" height="4" viewBox="0 0 6 4"><path d="M0 0l3 3 3-3" stroke="#9a3c28" fill="none"/></svg></div>
  <div class="abs btn" style="left:647px;top:18px;width:63px;height:19px;line-height:19px">Submit</div>
</section>

<h1 class="abs welcome-title">Welcome to Corwith Lodge</h1>
<div class="abs welcome-text">
  <p>Located in the heart of downtown Aspen, the newly renovated Corwith Lodge possesses all the charms of a vintage European Ski Lodge, while offering all of the modern conveniences one would expect with a stay in Aspen.</p>
  <p>A stay at our lodge includes free continental breakfast in our dining room, daily maid service, free wireless internet access,</p>
</div>
<div class="abs btn" style="left:228px;top:757px;width:83px;height:27px;line-height:27px">View More</div>
<div class="abs badge" role="img" aria-label="Certificate of excellence award badge" style="left:500px;top:665px;width:103px;height:83px;background:linear-gradient(180deg,#fff 0%,#fff 80%,#6aa85a 80%)"></div>
<div class="abs tour">Click here for a virtual<br>tour of the lodge!</div>
<div class="abs badge" role="img" aria-label="Top bed and breakfast listing badge" style="left:619px;top:665px;width:70px;height:112px;background:linear-gradient(180deg,#d8e8cc 0%,#7fb46c 70%,#d07a2a 92%)"></div>

<aside class="abs offer">
  <div class="offer-photo" role="img" aria-label="Guest room with red pillows on a patterned bed">
    <div class="offer-heading">Special Offer</div>
    <div class="offer-band"></div>
    <div class="offer-small">Stay 3 Nights<br>Get the 4th Night</div>
    <div class="offer-free">FREE!</div>
  </div>
</aside>

<section class="abs band"></section>
<h2 class="abs col-title" style="left:231px">Amenities</h2>
<p class="abs band-text" style="left:230px;top:862px;width:200px;font-weight:600;font-size:10.5px">The Corwith Lodge has many features for our guests to enjoy including:</p>
<ul class="abs band-list band-text">
  <li>Two Hot Tubs with fabulous views of Aspen Mountain and Red Mountain.</li>
  <li>Ski videos are shown in the evenings by the upper hot tub.</li>
  <li>High Speed Internet Access via Ethernet cable in every Room.</li>
</ul>
<div class="abs band-btn" style="left:230px">View More</div>

<h2 class="abs col-title" style="left:492px">Photogallery</h2>
<div class="abs gallery">
  <div class="abs" role="img" aria-label="Bedroom with carved wooden bed and quilt" style="left:5px;top:5px;width:120px;height:107px;background:linear-gradient(160deg,#5a3a26,#8a6a50 55%,#3a2a20)"></div>
  <div class="abs" role="img" aria-label="Bright guest room with bed" style="left:128px;top:16px;width:70px;height:41px;background:linear-gradient(160deg,#8a7a68,#c8b8a8)"></div>
  <div class="abs" role="img" aria-label="Room with red walls and bed" style="left:128px;top:60px;width:70px;height:41px;background:linear-gradient(160deg,#a8402e,#d8a89a)"></div>
  <svg class="abs" style="left:154px;top:4px" width="18" height="7" viewBox="0 0 18 7"><path d="M1 6l8-5 8 5" stroke="#3a2a20" stroke-width="2" fill="none"/></svg>
  <svg class="abs" style="left:154px;top:105px" width="18" height="7" viewBox="0 0 18 7"><path d="M1 1l8 5 8-5" stroke="#3a2a20" stroke-width="2" fill="none"/></svg>
</div>
<div class="abs band-btn" style="left:492px">View More</div>

<h2 class="abs col-title" style="left:751px">Latest Events</h2>
<div class="abs event-date" style="top:858px">30<small>Nov '12</small></div>
<div class="abs event-text" style="top:856px">Honour for sustainable student village in Bradford</div>
<div class="abs event-date" style="top:901px">30<small>Nov '12</small></div>
<div class="abs event-text" style="top:899px">Investment opportunities in Sub-Sahara Africa</div>
<div class="abs event-date" style="top:944px">30<small>Nov '12</small></div>
<div class="abs event-text" style="top:942px">Investment opportunities in Sub-Sahara Africa</div>
<div class="abs band-btn" style="left:751px">View More</div>

<footer>
  <div class="abs footer-links">Privacy Policy | Terms of Services | Sitemap<br>© Copyright 2012 All rights reserved.</div>
  <div class="abs social-label">Social Media:</div>
  <div class="abs social" style="left:846px"></div>
  <div class="abs social" style="left:875px"></div>
  <div class="abs social" style="left:904px"></div>
  <div class="abs social" style="left:933px"></div>
</footer>
</body>
</html>
```